Financial Service Company Need Business Card Design

This is a new startup company, first of its kind to offer this service. We facilitate the movement of deposit funds electronically between home buyers and real estate brokerages.Our customers are DOMIVANS®, real estate brokerages, and home buyers, we identify ourselves as a financial/technology company.
Not looking for anything too flashy. Just a clean design that shows the logo, contact info, etc. Company colors can be seen on attached logo, and 'coming soon page'
www.quorvanta.ca

```html
<!DOCTYPE html>
<html lang="en">
<head>
<meta charset="utf-8">
<title>Quorvanta Business Card</title>
<link rel="stylesheet" href="https://fonts.googleapis.com/css2?family=Exo+2:wght@400;500;600&display=swap">
<style>
  :root {
    --brand-orange: #ef5a2f;
    --brand-grey: #58595b;
    --panel-grey: #626366;
    --ribbon-grey: #8d8e90;
    --fold-grey: #4a4b4d;
    --card-white: #f7f7f7;
    --card-shade: #e4e4e5;
    --backdrop: #d9d9d7;
    --text-light: #ffffff;
  }
  html, body {
    margin: 0;
    width: 1200px;
    height: 869px;
    overflow: hidden;
    background: var(--backdrop);
    font-family: "Exo 2", sans-serif;
  }
  .canvas {
    position: relative;
    width: 1200px;
    height: 869px;
  }
  .card {
    position: absolute;
    width: 600px;
    height: 343px;
    box-shadow: 0 10px 24px rgba(0,0,0,0.18);
    overflow: hidden;
  }
  .card-front {
    left: 90px;
    top: 90px;
    background: linear-gradient(135deg, var(--card-white) 0%, var(--card-shade) 100%);
    display: flex;
    align-items: center;
    justify-content: center;
  }
  .wordmark {
    display: flex;
    align-items: center;
    gap: 14px;
  }
  .wordmark-square {
    background: var(--brand-orange);
  }
  .wordmark-name {
    color: var(--brand-grey);
    font-weight: 600;
    line-height: 1;
  }
  .card-front .wordmark-square { width: 46px; height: 46px; }
  .card-front .wordmark-name { font-size: 68px; }

  .card-back {
    left: 510px;
    top: 436px;
  }
  .card-shapes {
    position: absolute;
    inset: 0;
  }
  .card-back .wordmark {
    position: absolute;
    left: 36px;
    top: 50px;
    gap: 12px;
  }
  .card-back .wordmark-square { width: 30px; height: 30px; }
  .card-back .wordmark-name { font-size: 44px; }

  .address {
    position: absolute;
    left: 0;
    top: 156px;
    width: 400px;
    height: 29px;
    margin: 0;
    line-height: 29px;
    text-align: center;
    color: var(--text-light);
    font-size: 13px;
    letter-spacing: 0.5px;
  }
  .person {
    position: absolute;
    left: 440px;
    top: 150px;
    color: var(--brand-grey);
  }
  .person-name {
    font-size: 18px;
    font-weight: 500;
    letter-spacing: 1.5px;
    line-height: 1.1;
  }
  .person-title {
    font-size: 9px;
    letter-spacing: 1px;
    margin-top: 3px;
  }
  .contact {
    position: absolute;
    display: flex;
    align-items: center;
    gap: 10px;
    color: var(--text-light);
    font-size: 13px;
    letter-spacing: 0.4px;
  }
  .contact-icon {
    width: 20px;
    height: 20px;
    background: var(--text-light);
    border-radius: 3px;
    display: flex;
    align-items: center;
    justify-content: center;
  }
  .contact-icon svg { width: 14px; height: 14px; }
  .contact-web { left: 36px; top: 200px; }
  .contact-mail { left: 36px; top: 232px; }
  .contact-phone { left: 405px; top: 235px; }
  .contact-mobile { left: 405px; top: 264px; }
</style>
</head>
<body>
<main class="canvas">

  <section class="card card-front" aria-label="Card front">
    <div class="wordmark">
      <span class="wordmark-square"></span>
      <span class="wordmark-name">Quorvanta</span>
    </div>
  </section>

  <section class="card card-back" aria-label="Card back">
    <svg class="card-shapes" viewBox="0 0 600 343" width="600" height="343" aria-hidden="true">
      <defs>
        <linearGradient id="backFace" x1="0" y1="0" x2="1" y2="1">
          <stop offset="0" stop-color="#fbfbfb"/>
          <stop offset="1" stop-color="#dedede"/>
        </linearGradient>
      </defs>
      <rect width="600" height="343" fill="url(#backFace)"/>
      <polygon points="0,185 400,185 425,212 600,212 600,302 0,302" fill="var(--panel-grey)"/>
      <polygon points="400,156 425,212 400,185" fill="var(--fold-grey)"/>
      <rect x="0" y="156" width="400" height="29" fill="var(--ribbon-grey)"/>
      <rect x="0" y="302" width="600" height="41" fill="var(--brand-orange)"/>
    </svg>

    <div class="wordmark">
      <span class="wordmark-square"></span>
      <span class="wordmark-name">Quorvanta</span>
    </div>

    <p class="address">214, 9th floor, Harbour Line Road QVT</p>

    <div class="person">
      <div class="person-name">MARIN ALCOTT</div>
      <div class="person-title">GENERAL MANAGER</div>
    </div>

    <div class="contact contact-web">
      <span class="contact-icon">
        <svg viewBox="0 0 14 14" fill="none" stroke="var(--panel-grey)" stroke-width="1.2">
          <circle cx="7" cy="7" r="5.5"/>
          <ellipse cx="7" cy="7" rx="2.4" ry="5.5"/>
          <line x1="1.5" y1="7" x2="12.5" y2="7"/>
        </svg>
      </span>
      <span>www.quorvanta.ca</span>
    </div>

    <div class="contact contact-mail">
      <span class="contact-icon">
        <svg viewBox="0 0 14 14" fill="none" stroke="var(--panel-grey)" stroke-width="1.2">
          <rect x="1.5" y="3" width="11" height="8"/>
          <polyline points="1.5,3 7,8 12.5,3"/>
        </svg>
      </span>
      <span>hello@quorvanta.ca</span>
    </div>

    <div class="contact contact-phone">
      <span class="contact-icon">
        <svg viewBox="0 0 14 14" fill="var(--panel-grey)">
          <path d="M4 1.5 L6 4.5 L4.8 5.8 Q6 8.3 8.2 9.2 L9.5 8 L12.5 10 L11.2 12.3 Q6 12 2.7 6 Q2.2 3.2 4 1.5 Z"/>
        </svg>
      </span>
      <span>012 555 0148</span>
    </div>

    <div class="contact contact-mobile">
      <span class="contact-icon">
        <svg viewBox="0 0 14 14" fill="none" stroke="var(--panel-grey)" stroke-width="1.2">
          <rect x="4" y="1.5" width="6" height="11" rx="1"/>
          <line x1="6" y1="10.5" x2="8" y2="10.5"/>
        </svg>
      </span>
      <span>012 555 0148</span>
    </div>
  </section>

</main>
</body>
</html>
```